Copper Lantern Consulting Wordpress Website Design

I am looking for a wordpress website design for a consulting company called Copper Lantern Consulting. Services include SEO, social media campaign, PPC, and other online services. I want a media savvy looking website that is very easy to navigate but still looks professional. I'm essentially looking to have the clients say "wow" when they see the website but still can get an idea of the services they offer as a company. colour scheme should be blue and white primarily as the logo will be blue and white (in the midst of getting it finalized).

Target Market(s)

B2B, business owners and decision makers for SEO, PPC, Social Media, Etc.

Industry/Entity Type

Business Consultant

Colors
0293ce
33a6d7
0255a3
3276b5
85acd3
ffffff

Requirements
Must have
• Must look sleek and "techy" but at the same time look stylish and media savvy.
Nice to have
• blue and white as the colour scheme to a degree. Just an idea considering the logo will be blue and white. Perhaps some nice high resolution photos, some sliders
• also looking for potentially having large icons that represent some of the services we provide so its easy for clients to know what we offer.
Should not have
• bubbly and fun. This is more of a professional website.

```html
<!DOCTYPE html>
<html lang="en">
<head>
<meta charset="utf-8">
<title>Copper Lantern Consulting</title>
<link href="https://fonts.googleapis.com/css2?family=Open+Sans:ital,wght@0,400;0,600;0,700;1,400&display=swap" rel="stylesheet">
<style>
:root{
  --blue:#0293ce;
  --blue-light:#33a6d7;
  --blue-dark:#0255a3;
  --blue-mid:#3276b5;
  --blue-pale:#85acd3;
  --white:#ffffff;
  --ink:#333a40;
  --muted:#8a9096;
  --line:#e3e6e9;
  --footer:#eef0f2;
  --footer-bar:#e2e5e8;
}
*{box-sizing:border-box;margin:0;padding:0}
html,body{width:1200px;height:2332px;overflow:hidden}
body{font-family:"Open Sans",Arial,sans-serif;color:var(--ink);background:var(--white);position:relative}

/* header */
.site-header{height:48px;display:flex;align-items:center;justify-content:space-between;padding:0 52px 0 56px;border-top:3px solid var(--blue)}
.brand{font-size:24px;font-weight:700;color:var(--blue-dark)}
.main-nav{display:flex;gap:34px;font-size:13px}
.main-nav a{color:var(--ink);text-decoration:none;padding:14px 4px}
.main-nav a.active{color:var(--blue);border-bottom:2px solid var(--blue)}

/* hero */
.hero{position:relative;height:512px}
.hero-media{position:absolute;inset:0;background:linear-gradient(100deg,#c9dceb 0%,#eef3f7 35%,#dfe9f1 60%,#b9cfe0 100%)}
.slider-arrow{position:absolute;top:372px;width:36px;height:36px;border-radius:50%;background:rgba(40,60,80,.55);display:flex;align-items:center;justify-content:center}
.slider-arrow.prev{left:18px}
.slider-arrow.next{right:18px}

/* welcome */
.welcome{text-align:center;padding:46px 0 0;height:388px;position:relative}
.section-title{font-size:30px;font-weight:400;color:var(--blue)}
.section-title strong{font-weight:600}
.welcome p{width:700px;margin:22px auto 0;font-size:12.5px;line-height:22px;color:var(--muted)}
.btn{display:inline-flex;align-items:center;gap:10px;background:var(--blue-dark);color:var(--white);font-size:11px;font-weight:700;padding:9px 16px;letter-spacing:.5px;text-transform:uppercase}
.btn .tail{display:inline-block;width:16px;height:14px;background:var(--blue);margin-right:-8px}
.welcome .btn{margin-top:34px}
.divider{position:absolute;left:100px;right:100px;bottom:0;border-top:1px solid var(--line)}

/* services intro */
.services-intro{height:392px;display:flex;padding:50px 0 0 60px}
.team-media{width:480px;height:342px;background:linear-gradient(180deg,#f4f6f8 0%,#dfe3e8 55%,#c5ccd4 100%)}
.services-copy{padding:62px 0 0 80px;width:560px}
.services-copy .section-title{font-size:28px}
.services-copy p{margin-top:18px;font-size:12.5px;line-height:22px;color:var(--muted)}
.services-copy .btn{margin-top:58px}

/* service tiles */
.service-tiles{display:flex;height:260px}
.tile{flex:1;color:var(--white);text-align:center;padding:34px 36px 0}
.tile:nth-child(1){background:var(--blue-dark)}
.tile:nth-child(2){background:var(--blue-mid)}
.tile:nth-child(3){background:var(--blue)}
.tile:nth-child(4){background:var(--blue-light)}
.tile svg{height:60px}
.tile h3{font-size:17px;font-weight:400;margin-top:18px}
.tile p{font-size:11.5px;line-height:18px;margin-top:10px;opacity:.9}
.tile .more{display:block;font-size:10.5px;font-weight:700;margin-top:20px;letter-spacing:.5px;text-transform:uppercase}

/* testimonials */
.testimonials{height:340px;padding-top:44px;text-align:center}
.testimonials .section-title{font-size:28px}
.quotes{display:flex;gap:60px;padding:44px 100px 0;text-align:left}
.quote{flex:1;position:relative;padding-left:26px}
.quote::before{content:"\201C";position:absolute;left:0;top:-14px;font-size:54px;line-height:1;color:var(--blue);font-weight:700}
.quote p{font-size:12px;line-height:20px;color:var(--muted)}
.quote cite{display:block;margin-top:14px;font-size:12px;color:var(--blue)}

/* client row */
.clients{height:110px;border-top:1px solid var(--line);margin:0 100px;display:flex;align-items:center;justify-content:space-between;padding:0 30px}
.client{display:flex;align-items:center;gap:8px;font-size:20px;color:#555b61}
.client i{width:18px;height:18px;border-radius:50%;background:#555b61;display:inline-block}

/* footer */
.site-footer{position:absolute;left:0;right:0;top:2080px;height:252px;background:var(--footer)}
.footer-cols{display:flex;height:220px;padding:38px 100px 0}
.footer-col{flex:1}
.footer-col + .footer-col{border-left:1px solid #d6dadd;padding-left:40px}
.footer-col h4{font-size:13px;font-weight:700;color:var(--blue-dark);text-transform:uppercase;letter-spacing:.5px}
.footer-col p{font-size:11.5px;line-height:18px;color:var(--muted);margin-top:12px}
.signup{display:flex;margin-top:22px}
.signup span{width:170px;height:32px;background:var(--white);border:1px solid #d3d7db;font-size:11px;color:#aab0b5;padding:8px 10px}
.signup b{background:var(--blue);color:var(--white);font-size:11px;padding:9px 14px}
.news-time{color:var(--blue)}
.follow{text-align:center}
.socials{display:flex;gap:8px;justify-content:center;margin-top:18px}
.socials i{width:26px;height:26px;border-radius:50%;display:block}
.follow p{margin-top:18px}
.footer-bar{height:32px;background:var(--footer-bar)}
</style>
</head>
<body>

<header class="site-header">
  <div class="brand">Copper Lantern Consulting</div>
  <nav class="main-nav">
    <a class="active">Home</a><a>About Us</a><a>Services</a><a>Projects</a><a>Blog</a><a>Contact Us</a>
  </nav>
</header>

<section class="hero">
  <div class="hero-media" role="img" aria-label="Photo of a consulting team reviewing documents around an office table"></div>
  <span class="slider-arrow prev"><svg width="12" height="14" viewBox="0 0 12 14"><path d="M9 1 3 7l6 6" fill="none" stroke="#fff" stroke-width="2"/></svg></span>
  <span class="slider-arrow next"><svg width="12" height="14" viewBox="0 0 12 14"><path d="M3 1l6 6-6 6" fill="none" stroke="#fff" stroke-width="2"/></svg></span>
</section>

<section class="welcome">
  <h1 class="section-title">Welcome to <strong>Copper Lantern Consulting</strong></h1>
  <p>We help growing businesses reach the right audience online with measured strategy, clear reporting and campaigns built around real goals. Our team blends search, social and paid media into one plan, so every channel supports the next and every budget decision is backed by data you can read at a glance.</p>
  <a class="btn">Read More <span class="tail"></span></a>
  <div class="divider"></div>
</section>

<section class="services-intro">
  <div class="team-media" role="img" aria-label="Photo of a group of business professionals standing together"></div>
  <div class="services-copy">
    <h2 class="section-title">Our <strong>Services</strong></h2>
    <p>From first audit to ongoing growth, we plan, launch and refine digital campaigns for business owners who want clear results. Each service is tailored to your market, your customers and your goals, with honest advice at every step.</p>
    <a class="btn">Read More <span class="tail"></span></a>
  </div>
</section>

<section class="service-tiles">
  <div class="tile">
    <svg viewBox="0 0 60 60" width="60"><rect x="6" y="10" width="48" height="32" rx="2" fill="none" stroke="#fff" stroke-width="3"/><path d="M22 52h16M30 42v10" stroke="#fff" stroke-width="3"/><path d="M14 34l10-10 8 6 12-12" fill="none" stroke="#fff" stroke-width="3"/></svg>
    <h3>SEO</h3>
    <p>Climb search rankings with content and technical fixes that last.</p>
    <span class="more">Read More</span>
  </div>
  <div class="tile">
    <svg viewBox="0 0 60 60" width="60"><circle cx="30" cy="30" r="24" fill="none" stroke="#fff" stroke-width="3"/><circle cx="30" cy="24" r="6" fill="#fff"/><path d="M18 42c2-8 22-8 24 0" fill="#fff"/><circle cx="16" cy="28" r="4" fill="#fff"/><circle cx="44" cy="28" r="4" fill="#fff"/></svg>
    <h3>Social Media Campaign</h3>
    <p>Grow an engaged audience across the platforms your buyers use.</p>
    <span class="more">Read More</span>
  </div>
  <div class="tile">
    <svg viewBox="0 0 60 60" width="60"><rect x="8" y="8" width="30" height="22" rx="2" fill="none" stroke="#fff" stroke-width="3"/><rect x="22" y="24" width="30" height="22" rx="2" fill="var(--blue)" stroke="#fff" stroke-width="3"/><path d="M30 52h14" stroke="#fff" stroke-width="3"/></svg>
    <h3>PPC</h3>
    <p>Paid search ads tuned daily for cost, reach and conversions.</p>
    <span class="more">Read More</span>
  </div>
  <div class="tile">
    <svg viewBox="0 0 60 60" width="60"><circle cx="30" cy="18" r="10" fill="#fff"/><path d="M12 50c2-14 34-14 36 0z" fill="#fff"/><rect x="18" y="38" width="24" height="6" fill="var(--blue-light)"/></svg>
    <h3>Online Services</h3>
    <p>Web, email and analytics support to round out your strategy.</p>
    <span class="more">Read More</span>
  </div>
</section>

<section class="testimonials">
  <h2 class="section-title">Client <strong>Testimonials</strong></h2>
  <div class="quotes">
    <blockquote class="quote"><p>Their team rebuilt our search presence in three months and our inbound leads have doubled. Clear reports, quick replies and real expertise.</p><cite>Dana Whitlow, City Name</cite></blockquote>
    <blockquote class="quote"><p>We finally understand where our ad budget goes. Costs are down, conversions are up and the monthly reviews are genuinely useful to us.</p><cite>Dana Whitlow, City Name</cite></blockquote>
    <blockquote class="quote"><p>Our social channels went from quiet to busy. The campaign ideas were smart, on brand and delivered right on schedule every time.</p><cite>Dana Whitlow, City Name</cite></blockquote>
  </div>
</section>

<section class="clients">
  <span class="client"><i></i>Northgate</span>
  <span class="client">Brindle</span>
  <span class="client"><i></i>Quarto</span>
  <span class="client">Maple Cup</span>
  <span class="client">Ellipse</span>
</section>

<footer class="site-footer">
  <div class="footer-cols">
    <div class="footer-col">
      <h4>Newsletter</h4>
      <p>Get monthly tips on search, social and paid media sent to your inbox.</p>
      <div class="signup"><span>Email address</span><b>Sign Up</b></div>
    </div>
    <div class="footer-col">
      <h4>Latest News</h4>
      <p>New guide: five quick checks to speed up your landing pages and lift conversions this quarter. <span class="news-time">2 hours ago</span></p>
    </div>
    <div class="footer-col follow">
      <h4>Follow Us</h4>
      <div class="socials"><i style="background:var(--blue-dark)"></i><i style="background:var(--blue-light)"></i><i style="background:var(--blue-mid)"></i><i style="background:var(--blue)"></i></div>
      <p>Copyright 2015 Copper Lantern Consulting</p>
    </div>
  </div>
  <div class="footer-bar"></div>
</footer>

</body>
</html>
```